This is for a poster that will be hanging in the window of a Men's Suit Store in the mall:
Size 4 feet wide by 6 feet high
Main point is: A sale on "Suits" or "Men's Suits" at 40%-60% off ( the 40%-60% off should be the focal point)
Some words that can be used are "Sale" or "Clearance Sale"
Some key words that can be used to make it urgent are "limited time offer" or something similar.
You can get creative, the point is for the customer to want to come into the store and buy a suit right away.
You may use a graphic (picture of a man in a suit). It is not necessary but if it looks good you can use it. (If you do use a picture, it should be of a modern fit or slim fit suit)
Sorry, the initial brief somehow got deleted from the project. Please see the updated brief.
Thanks
Reason: Project was closed for some reason, extended to give enough time to complete
Target Market(s)
Mostly Men ages 35-55
Industry/Entity Type
Store
Colors
Designer to choose colors to be used in the design.

```html
<!DOCTYPE html>
<html lang="en">
<head>
<meta charset="utf-8">
<title>Suit Sale Window Poster</title>
<link rel="stylesheet" href="https://fonts.googleapis.com/css2?family=Ubuntu:wght@400;500;700&display=swap">
<style>
  :root {
    --backdrop: #111111;
    --gold: #c0a265;
    --gold-shadow: #9e8658;
    --paper: #ffffff;
    --ink: #111111;
    --sale-red: #e8242a;
    --suit-dark: #2a2a2a;
    --suit-grey: #3c3c3c;
  }
  html, body {
    margin: 0;
    width: 1000px;
    height: 1200px;
    overflow: hidden;
    background: var(--backdrop);
    font-family: "Ubuntu", "Segoe UI", sans-serif;
  }
  .poster {
    position: absolute;
    left: 165px;
    top: 98px;
    width: 692px;
    height: 1035px;
    background: var(--gold);
    overflow: hidden;
  }
  .poster__shapes { position: absolute; inset: 0; }
  .headline {
    position: absolute;
    left: 0;
    width: 514px;
    margin: 0;
    text-align: center;
    color: var(--paper);
    font-weight: 700;
    line-height: 1;
    white-space: nowrap;
  }
  .headline--first { top: 72px; font-size: 68px; }
  .headline__sale { color: var(--sale-red); font-size: 96px; }
  .headline--second { top: 188px; font-size: 54px; }
  .discount {
    position: absolute;
    left: 40px;
    top: 270px;
    margin: 0;
    display: flex;
    align-items: baseline;
    color: var(--ink);
    font-weight: 400;
    line-height: 1;
    white-space: nowrap;
  }
  .discount__value { font-size: 86px; letter-spacing: -3px; }
  .discount__to { font-size: 28px; margin: 0 4px; }
  .discount__off {
    font-size: 30px;
    font-weight: 500;
    writing-mode: vertical-rl;
    transform: rotate(180deg);
    margin-left: 12px;
    align-self: center;
  }
  .urgency {
    position: absolute;
    left: 175px;
    top: 376px;
    margin: 0;
    color: var(--paper);
    font-size: 25px;
    font-weight: 500;
    white-space: nowrap;
  }
  .clearance {
    position: absolute;
    left: 628px;
    top: 100px;
    margin: 0;
    writing-mode: vertical-rl;
    font-size: 40px;
    font-weight: 400;
    color: var(--ink);
    line-height: 1;
    white-space: nowrap;
  }
  .clearance__sale { color: var(--sale-red); font-weight: 700; }
  .figure-art {
    position: absolute;
    left: 50px;
    top: 532px;
    width: 165px;
    height: 495px;
    background: var(--suit-dark);
    border-radius: 60px 60px 6px 6px;
  }
  .jacket-art {
    position: absolute;
    left: 420px;
    top: 542px;
    width: 245px;
    height: 305px;
    background: linear-gradient(180deg, #4a4a4a, var(--suit-grey));
    border-radius: 40px 40px 4px 4px;
  }
  .brand {
    position: absolute;
    left: 438px;
    top: 904px;
    display: flex;
    align-items: center;
    gap: 10px;
    color: var(--paper);
    font-size: 28px;
    font-weight: 500;
    line-height: 1;
    white-space: nowrap;
  }
  .brand__mark {
    width: 14px;
    height: 14px;
    background: var(--paper);
  }
</style>
</head>
<body>
  <main class="poster">
    <svg class="poster__shapes" width="692" height="1035" viewBox="0 0 692 1035" aria-hidden="true">
      <path fill="var(--gold-shadow)" d="M575,0 L692,0 L692,445 C640,432 570,412 540,388 C500,356 498,318 512,280 Z"/>
      <path fill="var(--paper)" d="M610,0 L692,0 L692,442 C650,430 590,415 555,388 C515,356 512,318 525,282 Z"/>
      <path fill="var(--gold-shadow)" d="M0,446 C60,438 110,445 160,458 L372,534 C405,548 415,575 405,612 L350,1035 L0,1035 Z"/>
      <path fill="var(--paper)" d="M0,452 C60,444 110,450 150,462 L335,552 C370,566 380,580 375,612 L325,1035 L0,1035 Z"/>
      <path fill="var(--ink)" d="M345,847 L692,847 L692,992 L345,992 L415,919 Z"/>
    </svg>

    <h1 class="headline headline--first">A <span class="headline__sale">SALE</span> on</h1>
    <h2 class="headline headline--second">Men's Suits at</h2>

    <p class="discount">
      <span class="discount__value">40%</span>
      <span class="discount__to">To</span>
      <span class="discount__value">60%</span>
      <span class="discount__off">OFF</span>
    </p>

    <p class="urgency">Limited Time Offer</p>

    <p class="clearance">Clearance <span class="clearance__sale">Sale</span></p>

    <div class="figure-art" role="img" aria-label="Silhouette of a man in a slim-fit suit holding a briefcase"></div>
    <div class="jacket-art" role="img" aria-label="Charcoal suit jacket with white shirt and dotted tie"></div>

    <div class="brand">
      <span class="brand__mark" aria-hidden="true"></span>
      <span class="brand__name">harlan menswear</span>
    </div>
  </main>
</body>
</html>
```